After-School Program - End of the Year Mailing to Donors

We would like to highlight some of our accomplishments from the year and ask people to donate to our organization. We are a non-profit organization that serves underprivileged children with after school programs. We want a 6x9 flyer with printing on both sides that we can mail out soon. The flyer should be a mix of great photos, some text, and a space for mailing and return address.

Target Market(s)

regular donors

Industry/Entity Type

Education

Font styles to use
Serif

Colors

Designer to choose colors to be used in the design.

Requirements
Must have
• Photos, text, a space on one side for a mailing label, a return address, and a stamp.
Nice to have
• attractive, eye-catching
Should not have
• boring

```html
<!DOCTYPE html>
<html lang="en">
<head>
<meta charset="utf-8">
<title>Maple Street Family Center – Donor Postcard</title>
<link rel="stylesheet" href="https://fonts.googleapis.com/css2?family=Roboto+Slab:wght@400;500&family=Lato:wght@400;700&family=Kalam:wght@400&display=swap">
<style>
  :root{
    --bg:#3a3a3a;
    --teal:#3f8f9c;
    --teal-dark:#2f7683;
    --gold:#f2b92b;
    --navy:#1d3557;
    --ink:#2a2a2a;
    --panel:#f2f2f2;
    --paper:#ffffff;
    --tag:#d9472b;
    --rule:#b9b9b9;
  }
  *{margin:0;padding:0;box-sizing:border-box}
  html,body{width:1200px;height:1200px;overflow:hidden;background:var(--bg)}
  .card{position:absolute;left:210px;width:782px;height:520px;overflow:hidden;box-shadow:0 8px 24px rgba(0,0,0,.45)}
  .card--front{top:76px;background:var(--teal)}
  .card--back{top:636px;background:var(--paper)}
  .card svg.shapes{position:absolute;left:0;top:0}
  .headline{position:absolute;right:154px;top:110px;text-align:right;font-family:"Roboto Slab",serif;color:var(--ink)}
  .headline__sub{font-size:18px;line-height:24px}
  .headline__main{font-size:31px;line-height:42px;color:var(--navy);font-weight:500;letter-spacing:.5px}
  .org-name{position:absolute;font-family:"Roboto Slab",serif;color:var(--ink);text-align:center;font-size:11px;line-height:14px;display:flex;flex-direction:column;align-items:center;gap:6px}
  .org-name__dot{width:16px;height:16px;border-radius:50%;background:var(--gold)}
  .org-name--front{left:655px;top:112px;width:115px}
  .org-name--back{left:535px;top:72px;width:110px}
  .site-url{position:absolute;right:18px;top:493px;font-family:Lato,sans-serif;font-size:11px;color:#fff;letter-spacing:.4px}
  .about{position:absolute;left:40px;top:196px;width:372px;font-family:Lato,sans-serif;color:var(--ink)}
  .section-title{font-family:Lato,sans-serif;font-weight:700;font-size:16px;color:var(--teal-dark);margin-bottom:6px}
  .about p{font-size:10.2px;line-height:13px;text-align:justify}
  .about p + p{margin-top:8px}
  .about a{color:var(--teal-dark);text-decoration:none}
  .contact{position:absolute;left:38px;top:355px;font-family:Lato,sans-serif;color:var(--ink);font-size:10.5px;line-height:13px}
  .contact__row{display:flex;gap:8px;align-items:flex-start;margin-top:12px}
  .contact__row svg{flex:none;margin-top:1px}
  .tag{position:absolute;left:245px;top:390px;width:218px;height:80px;background:var(--tag);transform:rotate(-22deg);border-radius:4px;font-family:Kalam,cursive;color:#fff;text-align:center}
  .tag__inner{position:absolute;inset:6px;border:1.5px dashed #fff;border-radius:3px;padding:5px 8px 0 26px}
  .tag__hole{position:absolute;left:10px;top:32px;width:14px;height:14px;border-radius:50%;background:#fff;border:2px solid var(--teal)}
  .tag__line{font-size:13px;line-height:14px}
  .tag__phone{font-size:20px;line-height:25px;margin-top:2px}
</style>
</head>
<body>

<section class="card card--front" aria-label="Postcard front">
  <svg class="shapes" width="782" height="520" viewBox="0 0 782 520">
    <defs>
      <linearGradient id="groupPhoto" x1="0" y1="0" x2="0" y2="1">
        <stop offset="0" stop-color="#ffffff"/>
        <stop offset=".3" stop-color="#eef1ef"/>
        <stop offset=".45" stop-color="#c9d2c7"/>
        <stop offset=".55" stop-color="#8a9a85"/>
        <stop offset=".66" stop-color="#53608a"/>
        <stop offset=".76" stop-color="#6e6a80"/>
        <stop offset=".86" stop-color="#5e8f3f"/>
        <stop offset="1" stop-color="#74ad45"/>
      </linearGradient>
      <linearGradient id="stagePhoto" x1="0" y1="0" x2="0" y2="1">
        <stop offset="0" stop-color="#e4ddd2"/>
        <stop offset=".45" stop-color="#c9b89c"/>
        <stop offset=".7" stop-color="#6f8a6a"/>
        <stop offset="1" stop-color="#4a3a2c"/>
      </linearGradient>
      <radialGradient id="costumePhoto" cx=".5" cy=".6" r=".6">
        <stop offset="0" stop-color="#b58870"/>
        <stop offset=".5" stop-color="#5a3b34"/>
        <stop offset="1" stop-color="#151213"/>
      </radialGradient>
      <linearGradient id="classPhoto" x1="0" y1="0" x2="0" y2="1">
        <stop offset="0" stop-color="#cfe0d8"/>
        <stop offset=".3" stop-color="#8fb08a"/>
        <stop offset=".55" stop-color="#c8a48a"/>
        <stop offset=".8" stop-color="#2c3a5c"/>
        <stop offset="1" stop-color="#1c2440"/>
      </linearGradient>
    </defs>
    <g role="img" aria-label="Large group photo of children and staff sitting on a lawn in front of a playground">
      <path d="M42 390 C 42 300, 90 250, 170 150 C 240 128, 340 130, 400 120 C 470 110, 500 70, 560 45 C 640 18, 720 30, 782 55 L 782 490 C 600 494, 300 500, 85 498 C 55 495, 42 480, 42 460 Z" fill="url(#groupPhoto)" stroke="var(--gold)" stroke-width="4"/>
    </g>
    <rect x="0" y="498" width="782" height="22" fill="var(--teal)"/>
    <g stroke="var(--gold)" stroke-width="4">
      <circle cx="150" cy="135" r="98" fill="url(#stagePhoto)" role="img" aria-label="Photo of students playing trombone and violin on stage"/>
      <circle cx="118" cy="293" r="87" fill="url(#costumePhoto)" role="img" aria-label="Photo of three girls in costume with crowns performing"/>
      <circle cx="260" cy="225" r="92" fill="url(#classPhoto)" role="img" aria-label="Photo of a class of children in uniforms outdoors"/>
    </g>
  </svg>

  <div class="headline">
    <div class="headline__sub">Educational and</div>
    <div class="headline__sub">community building programs</div>
    <div class="headline__main">FOR CHILDREN</div>
  </div>

  <div class="org-name org-name--front">
    <span class="org-name__dot"></span>
    <span>Maple Street Family Center</span>
  </div>

  <div class="site-url">www.brightpathkids.org</div>
</section>

<section class="card card--back" aria-label="Postcard back">
  <svg class="shapes" width="782" height="520" viewBox="0 0 782 520">
    <defs>
      <linearGradient id="reindeerPhoto" x1="0" y1="0" x2="0" y2="1">
        <stop offset="0" stop-color="#8fa3c4"/>
        <stop offset=".35" stop-color="#d9d6d9"/>
        <stop offset=".6" stop-color="#8a5a48"/>
        <stop offset="1" stop-color="#c02a30"/>
      </linearGradient>
      <linearGradient id="boysPhoto" x1="0" y1="0" x2="0" y2="1">
        <stop offset="0" stop-color="#c9d6c4"/>
        <stop offset=".35" stop-color="#9a7a62"/>
        <stop offset=".65" stop-color="#27492f"/>
        <stop offset="1" stop-color="#1d3a25"/>
      </linearGradient>
    </defs>
    <rect x="0" y="0" width="452" height="520" fill="var(--panel)"/>
    <path d="M0 0 H782 V12 C 690 12, 590 12, 470 22 C 360 34, 300 56, 200 88 C 95 122, 40 160, 0 194 Z" fill="var(--teal)"/>
    <path d="M0 194 C 40 160, 95 122, 200 88 C 300 56, 360 34, 470 22 C 590 12, 690 12, 782 12" fill="none" stroke="var(--gold)" stroke-width="4"/>
    <g stroke="var(--gold)" stroke-width="4">
      <circle cx="145" cy="122" r="66" fill="url(#reindeerPhoto)" role="img" aria-label="Photo of two girls wearing paper reindeer antlers"/>
      <circle cx="284" cy="106" r="84" fill="url(#boysPhoto)" role="img" aria-label="Photo of two smiling boys in school uniforms"/>
    </g>
    <rect x="673" y="52" width="76" height="88" fill="none" stroke="#999" stroke-width="1"/>
    <g stroke="var(--rule)" stroke-width="1">
      <line x1="483" y1="229" x2="755" y2="229"/>
      <line x1="483" y1="267" x2="755" y2="267"/>
      <line x1="483" y1="306" x2="755" y2="306"/>
      <line x1="483" y1="347" x2="755" y2="347"/>
    </g>
    <path d="M272 437 C 245 443, 245 420, 262 416 M262 416 C 276 430, 292 438, 312 436" fill="none" stroke="var(--teal)" stroke-width="5" stroke-linecap="round"/>
    <rect x="0" y="492" width="782" height="4" fill="var(--gold)"/>
    <rect x="0" y="500" width="782" height="20" fill="var(--teal)"/>
  </svg>

  <div class="about">
    <h2 class="section-title">ABOUT US</h2>
    <p>Maple Street Family Center is in the middle of its 24th year of ministry and we need your help to finish our year strong! We need another $35,000 from our individual donors to help us meet our budget. We serve over 150 children each day at our four sites with a unique mix of homework help, a focus on literacy, enrichment classes - including music lessons, and a caring environment based on God's love. Please help us continue to impact children and families through our high quality faith-based educational programs.</p>
    <p>To contribute, please <a>visit www.brightpathkids.org</a> and click on the donate button.</p>
  </div>

  <div class="contact">
    <h2 class="section-title">CONTACT US</h2>
    <div class="contact__row">
      <svg width="12" height="14" viewBox="0 0 12 14"><path d="M6 1a4.5 4.5 0 0 0-4.5 4.5C1.5 9 6 13 6 13s4.5-4 4.5-7.5A4.5 4.5 0 0 0 6 1z" fill="none" stroke="var(--navy)" stroke-width="1.5"/><circle cx="6" cy="5.5" r="1.6" fill="var(--navy)"/></svg>
      <span>Maple Street Family Center 48 N.<br>Linden Ave. Fairview, CA 90210</span>
    </div>
    <div class="contact__row">
      <svg width="12" height="12" viewBox="0 0 12 12"><path d="M2.5 1l2 2.2-1 1.4a7 7 0 0 0 3.9 3.9l1.4-1 2.2 2-1.2 1.5C5.6 11 1 6.4 1 2.2z" fill="var(--navy)"/></svg>
      <span>(555) 274-0193</span>
    </div>
    <div class="contact__row">
      <svg width="12" height="12" viewBox="0 0 12 12"><circle cx="6" cy="6" r="5" fill="none" stroke="var(--navy)" stroke-width="1.4"/><path d="M1 6h10M6 1c2 2 2 8 0 10M6 1c-2 2-2 8 0 10" fill="none" stroke="var(--navy)" stroke-width="1"/></svg>
      <span>www.brightpathkids.org</span>
    </div>
  </div>

  <div class="tag">
    <span class="tag__hole"></span>
    <div class="tag__inner">
      <div class="tag__line">if you want to donate</div>
      <div class="tag__line">contact</div>
      <div class="tag__phone">(555) 274-0193</div>
    </div>
  </div>

  <div class="org-name org-name--back">
    <span class="org-name__dot"></span>
    <span>Maple Street Family Center</span>
  </div>
</section>

</body>
</html>
```